Real Estate 24"x24" Sign, Business Card, Letter Head and Envelope

This is a 4 project contest. If we choose a design or designs we like from what you sent we are willing to pay an amount at our discretion for that design even if we don't like all your designs for the 4 projects. Please be creative. Attached are our logo files. Please message us with any questions. Thanks and Good Luck!
Project 1: QLTV Realty 24" x 24" yard sign
We want to use the same blue background in our logo for the sign where the logo in white font will be on. CMYK 100,80,0,0. Attached is a sample a local designer made for you to get an idea what we are looking for. In the sample, the website is way too big and the entire sign is very plain and not attractive looking plus blue color is wrong one. We want the logo on top as large as possible but keeping it proportionate and attractive looking buy not too big that it looks odd. The following information can go in white color background or same blue color background color. Our company colors are blue (as per logo), green (as per logo), and white. "Residential & Commercial" goes under the logo. Under that put our phone number "312-948-6051" as large as possible but still looks good and under that our website in much smaller but readable font "www.qltvrealty.com".
Project 2: Envelope
We have two version of the logo. Use one or both. Whatever looks best in your design. The envelope will be white. We only want on top left corner logo and underneath our mailing address: 5197 Larchmere Ave. Skokie, IL 60093-1725. Maybe some creative decorative design at bottom of envelope will look nice
Project 3: Letter Head
We have two version of the logo. Use one or both. Whatever looks best in your design. We want the following information on the top of the letterhead. Logo, address: 5197 Larchmere Ave., Skokie, IL 60093-1725, phone: 312-948-6051, fax: 312-682-9307 website www.qltvrealty.com, email: info@qltvrealty.com
Project 4: Business card
Use either logo. We need cards for two individuals. Information for Person 1: Dev Kulkarni, Managing Broker, Phone: 312-948-6051, Email: dev.kulkarni@qltvrealty.com. Person 2: Ajay Kulkarni Broker Phone: 312-519-8263 Email: ajay.kulkarni@qltvrealty.com. Add Address, Fax and website same as above letter head.

```html
<!DOCTYPE html>
<html lang="en">
<head>
<meta charset="utf-8">
<title>QLTV Realty – Yard Sign Options</title>
<link href="https://fonts.googleapis.com/css2?family=Montserrat:wght@600&family=Playfair+Display:wght@400&display=swap" rel="stylesheet">
<style>
  :root {
    --brand-blue: #0a4595;
    --brand-green: #7dba43;
    --sign-white: #ffffff;
    --backdrop: #2c2c2c;
  }
  html, body {
    margin: 0;
    padding: 0;
    width: 1200px;
    height: 901px;
    overflow: hidden;
    background: var(--backdrop);
  }
  .sign-row {
    position: absolute;
    top: 273px;
    left: 0;
    width: 1200px;
    height: 352px;
  }
  .yard-sign {
    position: absolute;
    top: 0;
    width: 350px;
    height: 352px;
    display: block;
  }
  .sign-white-frame { left: 58px; }
  .sign-green-band { left: 424px; }
  .sign-full-blue { left: 792px; }
  .brand-name {
    font-family: "Montserrat", sans-serif;
    font-weight: 600;
    font-size: 32px;
    letter-spacing: 2px;
  }
  .service-line {
    font-family: "Playfair Display", serif;
    font-size: 22px;
  }
  .phone-number {
    font-family: "Playfair Display", serif;
    font-size: 62px;
  }
  .web-address {
    font-family: "Montserrat", sans-serif;
    font-weight: 600;
    font-size: 14px;
    letter-spacing: 0.5px;
  }
  .fill-blue { fill: var(--brand-blue); }
  .fill-green { fill: var(--brand-green); }
  .fill-white { fill: var(--sign-white); }
</style>
</head>
<body>
<main class="sign-row">

  <!-- White frame version -->
  <svg class="yard-sign sign-white-frame" viewBox="0 0 350 352" aria-label="QLTV Realty yard sign, blue on white">
    <rect class="fill-white" x="0" y="0" width="350" height="352"/>
    <rect class="fill-blue" x="9" y="9" width="332" height="170"/>
    <g class="brand-mark">
      <rect class="fill-white" x="42" y="83" width="18" height="18"/>
      <text class="brand-name fill-white" x="72" y="104" textLength="236" lengthAdjust="spacingAndGlyphs">QLTV REALTY</text>
    </g>
    <path class="fill-blue" d="M9 184 H341 V302 Q175 284 9 302 Z"/>
    <text class="service-line fill-white" x="175" y="216" text-anchor="middle" textLength="290" lengthAdjust="spacingAndGlyphs">RESIDENTIAL &amp; COMMERCIAL</text>
    <text class="phone-number fill-white" x="175" y="276" text-anchor="middle" textLength="300" lengthAdjust="spacingAndGlyphs">312-948-6051</text>
    <text class="web-address fill-blue" x="175" y="331" text-anchor="middle">QLTVREALTY.COM</text>
  </svg>

  <!-- Green band version -->
  <svg class="yard-sign sign-green-band" viewBox="0 0 350 352" aria-label="QLTV Realty yard sign, blue and green on white">
    <rect class="fill-white" x="0" y="0" width="350" height="352"/>
    <rect class="fill-blue" x="9" y="9" width="332" height="170"/>
    <g class="brand-mark">
      <rect class="fill-white" x="42" y="83" width="18" height="18"/>
      <text class="brand-name fill-white" x="72" y="104" textLength="236" lengthAdjust="spacingAndGlyphs">QLTV REALTY</text>
    </g>
    <path class="fill-green" d="M9 184 H341 V302 Q175 284 9 302 Z"/>
    <text class="service-line fill-white" x="175" y="216" text-anchor="middle" textLength="290" lengthAdjust="spacingAndGlyphs">RESIDENTIAL &amp; COMMERCIAL</text>
    <text class="phone-number fill-white" x="175" y="276" text-anchor="middle" textLength="300" lengthAdjust="spacingAndGlyphs">312-948-6051</text>
    <text class="web-address fill-blue" x="175" y="331" text-anchor="middle">QLTVREALTY.COM</text>
  </svg>

  <!-- Full blue version -->
  <svg class="yard-sign sign-full-blue" viewBox="0 0 350 352" aria-label="QLTV Realty yard sign, full blue with green base">
    <rect class="fill-blue" x="0" y="0" width="350" height="352"/>
    <g class="brand-mark">
      <rect class="fill-white" x="42" y="83" width="18" height="18"/>
      <text class="brand-name fill-white" x="72" y="104" textLength="236" lengthAdjust="spacingAndGlyphs">QLTV REALTY</text>
    </g>
    <rect class="fill-white" x="40" y="186" width="270" height="2"/>
    <text class="service-line fill-white" x="175" y="220" text-anchor="middle" textLength="270" lengthAdjust="spacingAndGlyphs">RESIDENTIAL &amp; COMMERCIAL</text>
    <text class="phone-number fill-white" x="175" y="280" text-anchor="middle" textLength="286" lengthAdjust="spacingAndGlyphs">312-948-6051</text>
    <path class="fill-green" d="M0 306 Q175 282 350 306 V352 H0 Z"/>
    <text class="web-address fill-white" x="175" y="334" text-anchor="middle">QLTVREALTY.COM</text>
  </svg>

</main>
</body>
</html>
```